Professional Business Cards

We need a nice looking, profession and modern business card for our new company. Our logo is attatched

Target Market(s)

Young Professionals

Industry/Entity Type

Financial

Contact Information for Business Card

FRONT

Vardane Ledger Pty Ltd
Level 22, Harbour Point, 48 Wattlebrook Ave
Sydney NSW 2000
ABN : 47 318 905 226

Owen Hadley - Chief Operations Officer
P : 02 9173 5528
M: 0418 356 091
owen@vardaneledger,com

BACK

- Cryptocurrency Exchange Services
- Cryptocurrency Mining Operations
- Cryptocurrency Investment Fund Offering

Font styles to use
Sans Serif

Colors
0255a3
9d9d9d

```html
<!DOCTYPE html>
<html lang="en">
<head>
<meta charset="utf-8">
<title>Vardane Ledger — Business Cards</title>
<link rel="stylesheet" href="https://fonts.googleapis.com/css2?family=Open+Sans:wght@400;600;700;800&display=swap">
<style>
  :root {
    --brand-blue: #0255a3;
    --brand-blue-light: #1a73c9;
    --brand-grey: #9d9d9d;
    --steel-light: #b3b8bc;
    --steel-dark: #6c7176;
    --paper: #ffffff;
    --backdrop: #2a2a2c;
    --text-on-blue: #ffffff;
  }
  * { box-sizing: border-box; margin: 0; padding: 0; }
  html, body { width: 1200px; height: 840px; overflow: hidden; }
  body {
    background: var(--backdrop);
    font-family: "Open Sans", Arial, sans-serif;
    position: relative;
  }
  .card {
    position: absolute;
    width: 560px;
    height: 342px;
    overflow: hidden;
    box-shadow: 0 14px 30px rgba(0,0,0,0.45);
  }

  /* Back of card */
  .card-back {
    left: 170px;
    top: 64px;
    background: linear-gradient(100deg, var(--steel-light) 0%, #8c9196 45%, var(--steel-dark) 100%);
    display: flex;
    align-items: center;
    justify-content: center;
  }
  .wordmark {
    display: flex;
    align-items: center;
    gap: 16px;
    font-weight: 800;
    letter-spacing: 3px;
    line-height: 1;
    white-space: nowrap;
  }
  .wordmark-square { display: block; }
  .card-back .wordmark { color: var(--paper); font-size: 46px; }
  .card-back .wordmark-square { width: 44px; height: 44px; background: var(--paper); }

  /* Front of card */
  .card-front {
    left: 470px;
    top: 434px;
    background: var(--paper);
  }
  .front-band { position: absolute; inset: 0; width: 100%; height: 100%; }
  .card-front .wordmark {
    position: absolute;
    left: 120px;
    top: 66px;
    color: var(--brand-blue);
    font-size: 30px;
    gap: 12px;
  }
  .card-front .wordmark-square { width: 29px; height: 29px; background: var(--brand-blue); }

  .company-address {
    position: absolute;
    right: 22px;
    top: 166px;
    text-align: right;
    color: var(--text-on-blue);
    font-style: normal;
    font-size: 12px;
    line-height: 1.5;
  }
  .company-address .company-name { font-weight: 700; }

  .person {
    position: absolute;
    left: 26px;
    top: 232px;
    color: var(--text-on-blue);
  }
  .person-name { font-size: 17px; font-weight: 700; letter-spacing: 0.3px; line-height: 1.2; }
  .person-title { font-size: 12.5px; margin-bottom: 4px; }
  .contact-list { list-style: none; font-size: 12.5px; line-height: 1.55; }
  .contact-list li { display: flex; align-items: center; gap: 8px; }
  .contact-icon { width: 12px; height: 12px; flex: none; fill: var(--text-on-blue); }
</style>
</head>
<body>

  <section class="card card-back" aria-label="Card back">
    <div class="wordmark">
      <span class="wordmark-square"></span>
      <span class="wordmark-name">VARDANE LEDGER</span>
    </div>
  </section>

  <section class="card card-front" aria-label="Card front">
    <svg class="front-band" viewBox="0 0 560 342" preserveAspectRatio="none" aria-hidden="true">
      <defs>
        <linearGradient id="bandFill" x1="0" y1="1" x2="1" y2="0">
          <stop offset="0" stop-color="#0255a3"/>
          <stop offset="1" stop-color="#1a73c9"/>
        </linearGradient>
      </defs>
      <polyline points="0,208 190,208 204,192 218,205 560,98" fill="none" stroke="#9d9d9d" stroke-width="4"/>
      <polygon points="0,216 190,216 204,200 218,213 560,106 560,342 0,342" fill="url(#bandFill)"/>
    </svg>

    <div class="wordmark">
      <span class="wordmark-square"></span>
      <span class="wordmark-name">VARDANE LEDGER</span>
    </div>

    <address class="company-address">
      <div class="company-name">Vardane Ledger Pty Ltd</div>
      <div>Level 22, Harbour Point</div>
      <div>48 Wattlebrook Ave</div>
      <div>Sydney NSW 2000</div>
      <div>ABN : 47 318 905 226</div>
    </address>

    <div class="person">
      <div class="person-name">OWEN HADLEY</div>
      <div class="person-title">Business Development Manager (founder)</div>
      <ul class="contact-list">
        <li>
          <svg class="contact-icon" viewBox="0 0 12 12" aria-hidden="true"><path d="M1 4 Q6 0 11 4 L9.5 5.5 L8 4.5 L8 3.5 Q6 2.8 4 3.5 L4 4.5 L2.5 5.5 Z M2.5 6.5 L9.5 6.5 L10.5 11 L1.5 11 Z"/></svg>
          <span>02 9173 5528</span>
        </li>
        <li>
          <svg class="contact-icon" viewBox="0 0 12 12" aria-hidden="true"><path d="M3 0.5 H9 V11.5 H3 Z M4 1.8 V9.2 H8 V1.8 Z"/></svg>
          <span>0418 356 091</span>
        </li>
        <li>
          <svg class="contact-icon" viewBox="0 0 12 12" aria-hidden="true"><path d="M0.5 2.5 H11.5 V9.5 H0.5 Z M1.5 3.3 L6 6.5 L10.5 3.3 Z"/></svg>
          <span>owen@vardaneledger,com</span>
        </li>
      </ul>
    </div>
  </section>

</body>
</html>
```